Label for Green Tea extract tablets

I would like to get label designs for my green tea extract tablets. The bottle will be green probably (90%). 750 mg in each capsule, bottle will hold 120 tablets. people buying green tea are healthy aware and looking for something to help with aging, cancer, metabolism.
This is description which i have from manufacturer:
Green Tea is a powerful natural antioxidant and helps to maintain a healthy metabolism. It has been used in Chinese medicine for around 4,000 years. These tablets contain high quality green tea extract for maximum effect in one easy-to-take dose.
Some evidence suggests green tea may lower the chance of developing heart disease and certain types of cancer. It is also reported to increase the ratio of good (HDL) cholesterol to bad (LDL) cholesterol in the blood. Green Tea has also been claimed useful as a weight-loss aid by increasing your metabolic rate and by inducing thermogenesis.
I will add the logo soon.
I hope it helps a bit.
Thank you
Target Market(s)
All health carring adults
Colors
Designer to choose colors to be used in the design.
Requirements
Must have
- Green tea extract, as a name
- Manufacturer required details of the product
- Powerful antioxidant
- Digestive regulator
- Boosts immune system
- Regulated cholesterol in the blood
- Helps to fight cancer
- The safest dose to maximalise benefits
- Made in the UK with the flag
- Finest quality ingredients
- 120 capsules
- 750mg
- vegan
- vegetarian
Nice to have
- Nice picture, natural leaves, powder, tea tree plantation picture
Should not have
- Name of my company
- Considering downloaded file do not put any company name on the label, please

```html
<!DOCTYPE html>
<html lang="en">
<head>
<meta charset="utf-8">
<title>Green Tea Extract Label</title>
<link rel="stylesheet" href="https://fonts.googleapis.com/css2?family=Sancreek&family=Share+Tech+Mono&family=Roboto+Condensed:wght@400&display=swap">
<style>
  :root {
    --paper: #ffffff;
    --title-green: #1e5b1f;
    --band-teal: #21b08b;
    --band-text: #ffffff;
    --ink: #1a1a1a;
    --flag-blue: #1f3d8a;
    --flag-red: #d0242f;
    --flag-white: #ffffff;
  }
  html, body {
    margin: 0;
    padding: 0;
    overflow: hidden;
    background: var(--paper);
  }
  .label {
    position: relative;
    width: 1200px;
    height: 1000px;
    background: var(--paper);
    overflow: hidden;
  }
  .product-title {
    position: absolute;
    top: 100px;
    left: 0;
    width: 1200px;
    margin: 0;
    text-align: center;
    font-family: "Sancreek", serif;
    font-weight: 400;
    font-size: 104px;
    line-height: 1;
    letter-spacing: 4px;
    color: var(--title-green);
    text-shadow: 3px 4px 5px rgba(0,0,0,0.28);
  }
  .band {
    position: absolute;
    left: 0;
    width: 1200px;
    background: var(--band-teal);
    color: var(--band-text);
    font-family: "Share Tech Mono", monospace;
    text-transform: uppercase;
  }
  .benefits-band {
    top: 250px;
    height: 78px;
    font-size: 20px;
    letter-spacing: 3.4px;
    text-align: center;
    line-height: 27px;
    padding-top: 12px;
    box-sizing: border-box;
  }
  .benefits-band p { margin: 0; }
  .photo {
    position: absolute;
    top: 330px;
    height: 475px;
  }
  .photo-plantation {
    left: 0;
    width: 603px;
    background: linear-gradient(to bottom, #cfe6ee 0%, #bcd9e3 38%, #6f9a3a 48%, #3f7a1e 70%, #2c5e14 100%);
  }
  .photo-leaves {
    left: 607px;
    width: 593px;
    background: linear-gradient(135deg, #e9dcd3 0%, #cfae98 30%, #7fae45 55%, #4f8a24 100%);
  }
  .details-band {
    top: 808px;
    height: 68px;
    font-size: 22px;
    letter-spacing: 3.6px;
    line-height: 28px;
    padding: 8px 42px 0;
    box-sizing: border-box;
    display: flex;
    justify-content: space-between;
  }
  .details-band p { margin: 0; }
  .details-right { text-align: right; }
  .origin {
    position: absolute;
    top: 888px;
    left: 0;
    width: 1200px;
    text-align: center;
  }
  .origin-flag {
    display: block;
    margin: 0 auto;
    width: 126px;
    height: 70px;
  }
  .origin-text {
    margin: 4px 0 0;
    font-family: "Roboto Condensed", sans-serif;
    font-size: 19px;
    color: var(--ink);
  }
</style>
</head>
<body>
<div class="label">
  <h1 class="product-title">Green Tea Extract</h1>

  <div class="band benefits-band">
    <p>Antioxidant, boosts immune system, regulates digestion, lowers cholesterol,</p>
    <p>maintains healthy weight by improving metabolism, and helps fight cancer.</p>
  </div>

  <div class="photo photo-plantation" role="img" aria-label="Photograph of rolling rows of green tea bushes on a plantation under a pale blue sky"></div>
  <div class="photo photo-leaves" role="img" aria-label="Photograph of cupped hands holding freshly picked green tea leaves over a basket of leaves"></div>

  <div class="band details-band">
    <div class="details-left">
      <p>750 mg green tea extract per capsule</p>
      <p>120 capsules</p>
    </div>
    <div class="details-right">
      <p>Finest quality ingredients</p>
      <p>Suitable for vegans and vegetarians</p>
    </div>
  </div>

  <div class="origin">
    <svg class="origin-flag" viewBox="0 0 60 30" preserveAspectRatio="none" aria-label="United Kingdom flag">
      <clipPath id="flag-clip"><rect width="60" height="30"/></clipPath>
      <g clip-path="url(#flag-clip)">
        <rect width="60" height="30" fill="var(--flag-blue)"/>
        <path d="M0,0 L60,30 M60,0 L0,30" stroke="var(--flag-white)" stroke-width="6"/>
        <path d="M0,0 L60,30 M60,0 L0,30" stroke="var(--flag-red)" stroke-width="2"/>
        <path d="M30,0 V30 M0,15 H60" stroke="var(--flag-white)" stroke-width="10"/>
        <path d="M30,0 V30 M0,15 H60" stroke="var(--flag-red)" stroke-width="6"/>
      </g>
    </svg>
    <p class="origin-text">MADE IN THE UK</p>
  </div>
</div>
</body>
</html>
```